Lawyer health website (wordpress design) to improve well being/health for lawyers

I need a webdesign for personal website called www.plumcounselhub.net. Website will be focused on health/wellness for my profession (lawyers) and other professionals too. Will have a blog on a separate page, a calorie counter on first page, and forums for me to begin topics and users to post. Also want the ability to add and delete information on a consistent basis...especially news articles related to my profession. I will want the homepage to include both health related information - different articles and articles related to the professionl. Need a tab to link my vitaloop site. I like format of www.dailyvigornest.com and www.munchtallyhub.com and www.sourbarrister.com. My website will have a mix of these themes and will not be too sarcastic (sourbarrister) but fun and healthy, a place for other attorneys and professionals to go to support eachother in health and wellness and their profession. Will need these things for the website:

(1) Responsive design (can be viewed on mobile phones, ipads, ect.)
(2)Cross browser support
(3) Custom background and colors
(4) Allow admin to post on front end and to add pages and delete and add info
(5) All post will have social media share
(6)Admin can control what is posted on page so if someone comments admin can review it before its posted on articles...forums no control over that. If admin wants to I can change the review function.
(7) Users can sign in with social media accounts or create a user name and password
(8) I am a female attorney so I prefer it be a bit more feminine but I will encourage males to follow the page as well.
(9) Feature attorney of the month or week on a page. I think this would be cool to do on a separate page highlighting an attorney, their practice area, their fitness goals ect.

Target Market(s)

Attorneys

Industry/Entity Type

Health

Coding

Coded - Design and coding required

Number of Pages Required

5+ page

Font styles to use
Serif

Colors
cadf82
85cae6
0355a3
00a990

Requirements
Must have
• Home page with "Featured attorney" section in a corner of page so users can click on that pic to learn about that "Feautured attorney" and how he/she stays fit. Also, calorie counter on home page, blog, Contact Us Page, and Forum Page.
• I MUST HAVE ABILITY TO ADD/DELETE CONTENT ON MY WEBSITE ON A CONSISTENT BASIS.

```html
<!DOCTYPE html>
<html lang="en">
<head>
<meta charset="utf-8">
<title>Plum Counsel Hub</title>
<link rel="stylesheet" href="https://fonts.googleapis.com/css2?family=Open+Sans:wght@400;600;700;800&display=swap">
<style>
:root{
  --page:#eef6cf;
  --page-deep:#e2efb4;
  --teal:#1ee3cf;
  --teal-dark:#11c9b5;
  --teal-text:#14b8a6;
  --nav-green:#8dc63f;
  --blue:#0355a3;
  --sky:#85cae6;
  --ink:#222;
  --muted:#777;
  --line:#d6d6d6;
  --white:#fff;
  --panel:#f4f4f4;
}
*{box-sizing:border-box;margin:0;padding:0}
html,body{width:792px;height:1200px;overflow:hidden}
body{font-family:"Open Sans",Arial,sans-serif;color:var(--ink);background:var(--white);position:relative;font-size:7px}
.abs{position:absolute}
ul{list-style:none}

/* header */
.site-header{left:0;top:0;width:792px;height:76px;background:var(--page)}
.top-bar{right:132px;top:4px;display:flex;align-items:center;gap:5px}
.social-dot{width:11px;height:11px;border-radius:50%}
.make-contact{background:#eaf59a;border:1px solid #c9d86b;font-size:7px;padding:3px 6px;margin-left:3px;border-radius:2px}
.account-bar{right:132px;top:30px;display:flex;gap:12px;font-size:6.5px;font-weight:700;align-items:center}
.account-bar span{display:flex;align-items:center;gap:3px}
.main-nav{left:268px;top:52px;display:flex;gap:16px;font-size:7px;color:var(--nav-green)}
.search{left:564px;top:51px;display:flex}
.search .field{width:58px;height:11px;background:var(--white)}
.search .btn{width:38px;height:11px;background:var(--teal);color:var(--white);font-size:6px;text-align:center;line-height:11px}

/* hero */
.hero{left:0;top:76px;width:792px;height:246px;background:linear-gradient(180deg,#e5e9dc 0%,#c9d3b8 45%,#6f8a4c 62%,#59604e 78%,#3c3d3a 100%)}
.calorie-panel{left:132px;top:76px;width:173px;height:246px;background:rgba(255,255,255,.86);padding:10px 8px}
.calorie-panel h1{font-size:12.5px;font-weight:800;text-align:center;line-height:1.2}
.calorie-panel p.intro{font-size:5.3px;color:#444;text-align:center;line-height:1.35;margin:4px 0 7px}
.form-row{display:flex;align-items:center;height:18px;font-size:5.8px;font-weight:700}
.form-row label{width:60px}
.input{height:12px;background:var(--white);border:1px solid #ddd;font-size:5.5px;font-weight:400;display:flex;align-items:center;justify-content:center}
.unit{font-weight:400;margin-left:3px;color:#666}
.email-input{margin-top:2px;height:12px;background:var(--white);border:1px solid #ddd;font-size:5.5px;color:#999;padding-left:4px;line-height:10px}
.consent{display:flex;gap:3px;font-size:4.6px;color:#555;line-height:1.3;margin-top:4px}
.consent i{width:5px;height:5px;border:1px solid #999;flex:none;margin-top:1px}
.track-btn{display:block;margin:6px auto 0;width:83px;height:17px;background:var(--teal-dark);color:var(--white);font-size:6px;text-align:center;line-height:17px}
.hero-photo{left:305px;top:76px;width:487px;height:246px}

/* features */
.features{left:0;top:322px;width:792px;height:68px;background:var(--page-deep)}
.feature{top:336px;width:170px;display:flex;gap:6px}
.feature .dot{width:26px;height:26px;border-radius:50%;flex:none;margin-top:10px}
.feature h2{font-size:10px;font-weight:800;text-align:center;line-height:1.15}
.feature p{font-size:6px;color:var(--muted);text-align:center;line-height:1.3;margin-top:2px}

/* news */
.news-title{left:132px;top:398px;font-size:12px;color:var(--teal-text);font-weight:600}
.news-grid{left:132px;top:422px;width:372px;display:grid;grid-template-columns:repeat(3,1fr);column-gap:8px;row-gap:14px}
.news-item{display:flex;flex-wrap:wrap;gap:4px}
.news-thumb{width:30px;height:21px;background:linear-gradient(135deg,#f4d7b0,#caa06e)}
.news-head{width:80px}
.news-head h3{font-size:7px;color:var(--teal-text);font-weight:600;line-height:1.1}
.news-head .date{font-size:5.5px;font-style:italic;color:#444}
.news-item p{font-size:5.5px;color:#555;line-height:1.35;width:114px}
.view-all{left:301px;top:550px;font-size:7.5px;color:var(--teal-text)}

/* lists */
.list-block{top:580px;width:178px}
.list-block h4{font-size:7px;color:var(--blue);font-weight:400;border-bottom:2px solid var(--blue);padding-bottom:3px;width:178px}
.list-block ul{margin-top:6px}
.list-block li{font-size:5.5px;color:#666;height:13px}
.list-photo{width:60px;height:88px}

/* sidebar */
.follow-box{left:515px;top:400px;width:145px;height:48px;background:var(--teal)}
.follow-box h5{font-size:6.5px;color:var(--white);font-weight:600;padding:5px 6px}
.follow-icons{display:flex;gap:12px;padding-left:8px}
.follow-icons i{width:17px;height:17px;border-radius:50%;display:block}
.tabs{left:515px;top:463px;width:145px;display:flex}
.tabs span{flex:1;height:21px;font-size:6.5px;color:#666;background:#e6e6e6;line-height:21px;text-align:center}
.tabs span.on{background:var(--panel);color:#333}
.side-list{left:515px;top:484px;width:145px;height:156px;background:var(--panel);padding:6px 4px}
.side-item{display:flex;gap:4px;height:37px}
.date-badge{width:20px;height:20px;border-radius:50%;background:var(--teal-dark);color:var(--white);font-size:5.5px;font-weight:700;text-align:center;line-height:7px;padding-top:3px;flex:none}
.date-badge.light{background:#9ee4dc}
.side-item h6{font-size:5.5px;color:var(--teal-text);font-weight:400}
.side-item p{font-size:5.5px;color:#666;line-height:1.3}
.side-more{left:515px;top:651px;width:145px;height:12px;background:var(--teal-dark);color:var(--white);font-size:6px;font-weight:700;text-align:center;line-height:12px}

/* teal band */
.teal-band{left:0;top:718px;width:792px;height:153px;background:var(--teal)}
.band-card{top:735px;width:163px}
.band-card .pic{width:163px;height:83px}
.band-card h4{font-size:6.3px;color:var(--white);font-weight:800;margin-top:5px}
.band-card p{font-size:5.8px;color:var(--white);line-height:1.3}

/* about */
.about-art{left:150px;top:880px;width:220px;height:190px}
.about-box{left:371px;top:927px;width:290px;height:125px;border:1px solid var(--line);background:var(--white);padding:10px 14px}
.about-box h2{font-size:14px;color:var(--blue);font-weight:400;text-align:center;letter-spacing:.5px}
.about-box p{font-size:6px;color:#666;text-align:center;line-height:1.5;margin-top:7px}

/* contact */
.contact-band{left:0;top:1075px;width:792px;height:90px;background:var(--teal);color:var(--white)}
.contact-band h2{position:absolute;left:136px;top:10px;font-size:13px;font-weight:400}
.contact-intro{position:absolute;left:136px;top:36px;font-size:8.5px;line-height:1.2}
.contact-intro b{font-size:13px;font-weight:400;display:block}
.cf{position:absolute;display:flex;align-items:center;gap:3px;font-size:6.5px}
.cf i{display:block;height:11px;background:var(--white);border-radius:1px}
.send-btn{position:absolute;left:613px;top:1133px;width:46px;height:14px;border:1px solid var(--white);color:var(--white);font-size:7px;font-weight:700;text-align:center;line-height:12px}

/* footer */
.site-footer{left:0;top:1165px;width:792px;height:35px;background:var(--page);text-align:center}
.footer-nav{display:flex;justify-content:center;gap:14px;font-size:6.5px;padding-top:9px}
.copyright{font-size:5.5px;margin-top:2px}
</style>
</head>
<body>

<header class="site-header abs">
  <div class="top-bar abs">
    <i class="social-dot" style="background:#3b5c9c"></i>
    <i class="social-dot" style="background:#d33"></i>
    <i class="social-dot" style="background:#35a8e0"></i>
    <i class="social-dot" style="background:#1f6fa8"></i>
    <span class="make-contact">MAKE CONTACT</span>
  </div>
  <div class="account-bar abs">
    <span>Sign in
      <svg width="9" height="9" viewBox="0 0 10 10"><circle cx="5" cy="3" r="2.3" fill="#222"/><path d="M1 10c0-3 2-4.5 4-4.5S9 7 9 10z" fill="#222"/></svg>
    </span>
    <span>Contact us:
      <svg width="10" height="8" viewBox="0 0 10 8"><rect width="10" height="8" fill="#222"/><path d="M0 0l5 4 5-4" stroke="#fff" fill="none" stroke-width=".8"/></svg>
    </span>
    <span>Phone:1234 567 890</span>
  </div>
  <nav class="main-nav abs">
    <span>Home</span><span>About Us</span><span>forum ▸</span><span>Featured attorney</span><span>Contact Us</span><span>Blog</span>
  </nav>
  <div class="search abs"><span class="field"></span><span class="btn">SEARCH</span></div>
</header>

<section class="hero abs" aria-label="Calorie counter"></section>
<div class="hero-photo abs" role="img" aria-label="Photo of a runner in three stages, from out of shape to fit, on a country road" style="background:linear-gradient(180deg,rgba(240,240,225,.6),rgba(150,170,110,.2) 55%,rgba(60,60,55,.3))"></div>
<form class="calorie-panel abs">
  <h1>GET YOUR FREE CALORIE COUNTER NOW!</h1>
  <p class="intro">The Calorie Calculator can be used to estimate the calories you need to consume each day. This calculator can also provide some simple guideline if you want to gain or lose weight. Use the "metric units" tab if you are more comfortable with the international standard metric units.</p>
  <div class="form-row"><label>GENDER</label><span class="input" style="width:30px">Male</span><span class="input" style="width:30px;margin-left:6px">Female</span></div>
  <div class="form-row"><label>CURRENT WEIGHT</label><span class="input" style="width:30px"></span><span class="unit">lbs</span></div>
  <div class="form-row"><label>GOAL WEIGHT</label><span class="input" style="width:30px"></span><span class="unit">lbs</span></div>
  <div class="form-row"><label>HEIGHT</label><span class="input" style="width:30px">ft ▾</span><span class="input" style="width:30px;margin-left:6px">ft ▾</span></div>
  <div class="email-input">Enter your email</div>
  <div class="consent"><i></i><span>I would like Plum Counsel Hub news, tips and updates by email. You can unsubscribe at any time.</span></div>
  <span class="track-btn">Start Tracking Now</span>
</form>

<section class="features abs"></section>
<div class="feature abs" style="left:132px"><i class="dot" style="background:#5fd6c0;border:2px solid #b7ecdf"></i><div><h2>INTERDUM ET MALESU ADA FAMES AC</h2><p>ante ipsum primis in faucibus. Integer a mi vel nunc congue placerat.</p></div></div>
<div class="feature abs" style="left:313px"><i class="dot" style="background:#5b96cf;border:2px solid #b9d3ea"></i><div><h2>INTERDUM ET MALESU ADA FAMES AC</h2><p>ante ipsum primis in faucibus. Integer a mi vel nunc congue placerat.</p></div></div>
<div class="feature abs" style="left:495px"><i class="dot" style="background:#bfeae4;border:2px solid #dff4f0"></i><div><h2>INTERDUM ET MALESU ADA FAMES AC</h2><p>ante ipsum primis in faucibus. Integer a mi vel nunc congue placerat.</p></div></div>

<h2 class="news-title abs">NEWS</h2>
<div class="news-grid abs">
  <article class="news-item"><div class="news-thumb" role="img" aria-label="Thumbnail of a woman with fruit"></div><div class="news-head"><h3>Lorem ipsum dolor sit amet, consectetur</h3><div class="date">april 7, 2015</div></div><p>Consectetur nibh. Phasellus vitae dolor dolor. Praesent in lectus felis. Curabitur id lorem nec neque commodo</p></article>
  <article class="news-item"><div class="news-thumb" role="img" aria-label="Thumbnail of a woman with fruit"></div><div class="news-head"><h3>Lorem ipsum dolor sit amet, consectetur</h3><div class="date">april 7, 2015</div></div><p>Consectetur nibh. Phasellus vitae dolor dolor. Praesent in lectus felis. Curabitur id lorem nec neque commodo</p></article>
  <article class="news-item"><div class="news-thumb" role="img" aria-label="Thumbnail of a woman with fruit"></div><div class="news-head"><h3>Lorem ipsum dolor sit amet, consectetur</h3><div class="date">april 7, 2015</div></div><p>Consectetur nibh. Phasellus vitae dolor dolor. Praesent in lectus felis. Curabitur id lorem nec neque commodo</p></article>
  <article class="news-item"><div class="news-thumb" role="img" aria-label="Thumbnail of a woman with fruit"></div><div class="news-head"><h3>Lorem ipsum dolor sit amet, consectetur</h3><div class="date">april 7, 2015</div></div><p>Consectetur nibh. Phasellus vitae dolor dolor. Praesent in lectus felis. Curabitur id lorem nec neque commodo</p></article>
  <article class="news-item"><div class="news-thumb" role="img" aria-label="Thumbnail of a woman with fruit"></div><div class="news-head"><h3>Lorem ipsum dolor sit amet, consectetur</h3><div class="date">april 7, 2015</div></div><p>Consectetur nibh. Phasellus vitae dolor dolor. Praesent in lectus felis. Curabitur id lorem nec neque commodo</p></article>
  <article class="news-item"><div class="news-thumb" role="img" aria-label="Thumbnail of a woman with fruit"></div><div class="news-head"><h3>Lorem ipsum dolor sit amet, consectetur</h3><div class="date">april 7, 2015</div></div><p>Consectetur nibh. Phasellus vitae dolor dolor. Praesent in lectus felis. Curabitur id lorem nec neque commodo</p></article>
</div>
<span class="view-all abs">View all</span>

<section class="list-block abs" style="left:132px">
  <h4>FEATURED ATTORNEY</h4>
  <ul><li>• John Doe</li><li>• Joahn Doe</li><li>• Scelerisque eros in tempor blandit.</li><li>• Sed vestibulum pharetra nunc, et pha</li><li>• Retra arcu. Vestibulum sagittis nec</li><li>• Nisl vel porttitor. Suspendisse fauci</li><li>• Bus urna non velit rhoncus, non</li><li>• Vulputate nisl lacinia.</li></ul>
</section>
<div class="list-photo abs" style="left:248px;top:613px;background:linear-gradient(160deg,#d9dde2,#4a5260)" role="img" aria-label="Photo of the featured attorney in a suit"></div>
<section class="list-block abs" style="left:319px">
  <h4>BLOG THEMES</h4>
  <ul><li>• Lorem ipsum dolor sit</li><li>• Consectetur adipiscing elit</li><li>• Scelerisque eros in tempor</li><li>• Sed vestibulum pharetra</li><li>• Retra arcu. Vestibulum</li><li>• Nisl vel porttitor.</li><li>• Bus urna non velit rhoncus,</li></ul>
</section>
<div class="list-photo abs" style="left:415px;top:605px;width:83px;height:85px;background:linear-gradient(180deg,#f2f2f2 40%,#d8a56a 70%,#8fb34a)" role="img" aria-label="Photo of a woman with a clock and fresh vegetables"></div>

<aside>
  <div class="follow-box abs"><h5>FOLLOW US AROUND THE WEB</h5>
    <div class="follow-icons"><i style="background:#8a8a8a"></i><i style="background:#3b5c9c"></i><i style="background:#35a8e0"></i><i style="background:#d33"></i></div>
  </div>
  <div class="tabs abs"><span class="on">POPULAR</span><span>RECENT</span><span>RANDOM</span></div>
  <div class="side-list abs">
    <div class="side-item"><span class="date-badge">SAT<br>14</span><div><h6>INTERDUM ET MALESU ADA FAMES AC</h6><p>Ante ipsum primis in faucibus. Integer a mi vel nunc congue placerat.</p></div></div>
    <div class="side-item"><span class="date-badge light">SAT<br>14</span><div><h6>INTERDUM ET MALESU ADA FAMES AC</h6><p>Ante ipsum primis in faucibus. Integer a mi vel nunc congue placerat.</p></div></div>
    <div class="side-item"><span class="date-badge light">SAT<br>14</span><div><h6>INTERDUM ET MALESU ADA FAMES AC</h6><p>Ante ipsum primis in faucibus. Integer a mi vel nunc congue placerat.</p></div></div>
    <div class="side-item"><span class="date-badge">SAT<br>14</span><div><h6>INTERDUM ET MALESU ADA FAMES AC</h6><p>Ante ipsum primis in faucibus. Integer a mi vel nunc congue placerat.</p></div></div>
  </div>
  <span class="side-more abs">VIEW ALL</span>
</aside>

<section class="teal-band abs"></section>
<article class="band-card abs" style="left:132px"><div class="pic" role="img" aria-label="Photo of business people talking in an office" style="background:linear-gradient(135deg,#e9eef2,#7a8596)"></div><h4>LOREM IPSUM DOLOR SIT AMET CONSEC</h4><p>Lorem ipsum dolor sit amet, consectetur adipiscing elit. Nunc feugiat id arcu sed volutpat. Cras vel fermentum urna. Donec ut dui risus.</p></article>
<article class="band-card abs" style="left:315px"><div class="pic" role="img" aria-label="Photo of a couple cooking vegetables in a kitchen" style="background:linear-gradient(135deg,#f4f1ea,#b9c7a0)"></div><h4>LOREM IPSUM DOLOR SIT AMET CONSEC</h4><p>Lorem ipsum dolor sit amet, consectetur adipiscing elit. Nunc feugiat id arcu sed volutpat. Cras vel fermentum urna. Donec ut dui risus.</p></article>
<article class="band-card abs" style="left:497px"><div class="pic" role="img" aria-label="Photo of a woman preparing fruit at a table" style="background:linear-gradient(135deg,#b5683a,#6b3a22)"></div><h4>LOREM IPSUM DOLOR SIT AMET CONSEC</h4><p>Lorem ipsum dolor sit amet, consectetur adipiscing elit. Nunc feugiat id arcu sed volutpat. Cras vel fermentum urna. Donec ut dui risus.</p></article>

<div class="about-art abs" role="img" aria-label="Illustration of a hand drawing a healthy life diagram: exercise regularly, eat healthy, reduce stress, drink plenty of water" style="background:radial-gradient(circle at 40% 45%,#f6f8ee 0%,#eef3df 55%,#ffffff 80%)"></div>
<section class="about-box abs">
  <h2>PLUM COUNSEL HUB</h2>
  <p>Lorem ipsum dolor sit amet, consectetur adipiscing elit. Aenean bibendum lectus tellus, rhoncus aliquam odio laoreet non. Phasellus et aliquet leo, vitae dapibus libero. Class aptent taciti sociosqu ad litora torquent per conubia nostra, per inceptos himenaeos. Integer id augue eu dolor lobortis cursus.<br>Nunc in erat suscipit, vestibulum quam vel, vulputate nisi. Donec non eros vehicula, iaculis massa at, congue ligula. Nulla feugiat lacus nec augue rhoncus dapibus.</p>
</section>

<section class="contact-band abs">
  <h2>CONTACT PLUM COUNSEL HUB</h2>
  <div class="contact-intro">Please contact us on<b>1234 567 890</b>or fill out below</div>
  <div class="cf" style="left:254px;top:34px">First name:<i style="width:52px"></i></div>
  <div class="cf" style="left:379px;top:34px">Last name:<i style="width:52px"></i></div>
  <div class="cf" style="left:492px;top:34px">Email Address:<i style="width:52px"></i></div>
  <div class="cf" style="left:254px;top:60px">Primary Contact Phone:<i style="width:52px"></i></div>
  <div class="cf" style="left:393px;top:55px">How can we help you today?<i style="width:80px;height:22px"></i></div>
</section>
<span class="send-btn">SEND</span>

<footer class="site-footer abs">
  <nav class="footer-nav"><span>Home</span><span>About Us</span><span>forum &gt;</span><span>Featured attorney</span><span>Contact Us</span><span>Blog</span></nav>
  <div class="copyright">Copyright 2015</div>
</footer>

</body>
</html>
```